Rebrand stationary with recently completed logo design

Need new business cards, thank you cards, letterhead, envelopes and presentation folders. The designs will be sent to a separate production firm so I need the files to be print ready.

My contact info
Reno Vaskelind

Office 604-381-4756
Fax 604-318-5064

Email reno@glazeworks.ca
website www.glazeworks.ca

315-27140 62nd Avenue,
Langley, BC, V3K 2R8

Target Market(s)

Homeowners, businesses and contractors

Industry/Entity Type

Business

Font styles to use
Sans Serif

Colors
34a7d7

Requirements
Must have
• Like to have one side of the business card a solid color with the logo in all white. The side with all the text to be a white background
• I find the current blue on the front of the card with the white logo too dark.
Should not have
• Gradient colors

```html
<!DOCTYPE html>
<html lang="en">
<head>
<meta charset="utf-8">
<title>Glazeworks Stationery Set</title>
<link rel="stylesheet" href="https://fonts.googleapis.com/css2?family=Arimo&family=PT+Sans:ital@0;1&family=Titillium+Web:wght@400&family=Crimson+Text:ital@1&family=Great+Vibes&display=swap">
<style>
  :root {
    --canvas: #d3d4d6;
    --paper: #ffffff;
    --brand-blue: #1b98d5;
    --ink: #3f4a55;
    --body-ink: #555a60;
    --muted: #6e7278;
    --frame: #5d6166;
    --caption: #6a6d71;
  }
  * { margin: 0; padding: 0; box-sizing: border-box; }
  html, body { width: 1200px; height: 854px; overflow: hidden; }
  body { background: var(--canvas); position: relative; font-family: "Arimo", Arial, sans-serif; }
  .sheet { position: absolute; background: var(--paper); overflow: hidden; }
  .abs { position: absolute; }

  .wordmark { font-family: "Titillium Web", sans-serif; font-weight: 400; color: var(--ink); line-height: 1; white-space: nowrap; letter-spacing: .5px; }
  .contact { font-family: "PT Sans", sans-serif; font-style: italic; color: var(--body-ink); white-space: nowrap; }
  .accent { color: var(--brand-blue); }

  /* Letterhead */
  .letterhead { left: 26px; top: 36px; width: 559px; height: 790px; }
  .letterhead .wordmark { left: 26px; top: 88px; font-size: 24px; }
  .letterhead .contact { left: 420px; top: 36px; font-size: 11px; line-height: 13.5px; }
  .letter-body { left: 87px; top: 181px; width: 368px; font-size: 10px; line-height: 13.3px; letter-spacing: .1px; color: var(--body-ink); }
  .letter-body p { margin-bottom: 13.3px; }
  .signature { left: 87px; top: 585px; width: 95px; height: 42px; background: #eceef0; border-radius: 4px; }
  .sign-off { left: 87px; top: 638px; font-size: 10px; line-height: 13.3px; color: var(--body-ink); }
  .letterhead .web { left: 30px; top: 750px; font-size: 13px; }

  /* Business cards */
  .card-front { left: 600px; top: 37px; width: 254px; height: 151px; background: var(--brand-blue); }
  .card-front .wordmark { left: 67px; top: 88px; font-size: 20px; color: #fff; }
  .card-back { left: 876px; top: 34px; width: 254px; height: 152px; border: 1px solid var(--frame); }
  .card-back .wordmark { left: 21px; top: 96px; font-size: 14px; }
  .card-back .name { left: 146px; top: 56px; font-size: 13px; }
  .card-back .details { left: 147px; top: 75px; font-size: 8px; line-height: 10.6px; }
  .caption { left: 724px; top: 197px; font-size: 20px; color: var(--caption); font-family: "Arimo", sans-serif; }

  /* Envelope */
  .envelope { left: 519px; top: 242px; width: 582px; height: 268px; border: 1px solid #9a9ea3; border-right: none; }
  .envelope .wordmark { left: 16px; top: 86px; font-size: 24px; }
  .envelope .contact { left: 16px; top: 226px; font-size: 13px; line-height: 17px; }
  .envelope-flap { left: 1100px; top: 242px; width: 76px; height: 268px; }
  .flap-web { left: 1121px; top: 441px; transform: rotate(-90deg); transform-origin: left top; font-size: 13px; color: #fff; font-family: "PT Sans", sans-serif; font-style: italic; white-space: nowrap; }

  /* Thank-you card */
  .thanks-card { left: 629px; top: 528px; width: 481px; height: 280px; border: 1px solid var(--frame); }
  .thanks-title { left: 12px; top: 26px; font-family: "Great Vibes", cursive; font-size: 56px; color: var(--brand-blue); line-height: 1; white-space: nowrap; }
  .thanks-card .wordmark { left: 347px; top: 75px; font-size: 20px; }
  .poem { left: 31px; top: 111px; font-family: "Crimson Text", serif; font-style: italic; font-size: 12.5px; line-height: 16.5px; color: #333; }
  .signer { left: 31px; top: 213px; font-size: 15px; color: var(--muted); }
  .thanks-card .web { left: 31px; top: 252px; font-size: 9px; }
  .globe { display: inline-block; vertical-align: -1px; margin-right: 5px; }
</style>
</head>
<body>

  <!-- Letterhead -->
  <section class="sheet letterhead">
    <div class="abs wordmark">GLAZEWORKS</div>
    <div class="abs contact">604-381-4756<br>604-318-5064<br>reno@glazeworks.ca<br><span style="display:block;height:3px"></span>315-27140 62nd Avenue,<br>Langley, BC, V3K 2R8</div>
    <div class="abs letter-body">
      <p>Contrary to popular belief, Lorem Ipsum is not simply random text. It has roots in a piece of classical Latin literature from 45 BC, making it over 2000 years old. Alden Pryce, a Latin professor at Ashford Hill College in Virginia, looked up one of the more obscure Latin words, consectetur, from a Lorem Ipsum passage, and going through the cites of the word in classical literature, discovered the undoubtable source. Lorem Ipsum comes from sections 1.10.32 and 1.10.33 of "de Finibus Bonorum et Malorum" (The Extremes of Good and Evil) by Marcus Orvian, written in 45 BC. This book is a treatise on the theory of ethics, very popular during the Renaissance. The first line of Lorem Ipsum, "Lorem ipsum dolor sit amet..", comes from a line in section 1.10.32.</p>
      <p>The standard chunk of Lorem Ipsum used since the 1500s is reproduced below for those interested. Sections 1.10.32 and 1.10.33 from "de Finibus Bonorum et Malorum" by Marcus Orvian are also reproduced in their exact original form, accompanied by English versions from the 1914 translation by H. Welbourne.</p>
      <p>Where can I get some?<br>There are many variations of passages of Lorem Ipsum available, but the majority have suffered alteration in some form, by injected humour, or randomised words which don't look even slightly believable. If you are going to use a passage of Lorem Ipsum, you need to be sure there isn't anything embarrassing hidden in the middle of text. All the Lorem Ipsum generators on the Internet tend to repeat predefined chunks as necessary, making this the first true generator on the Internet. It uses a dictionary of over 200 Latin words, combined with a handful of model sentence structures, to generate Lorem Ipsum which looks reasonable. The generated Lorem Ipsum is therefore always free from repetition, injected humour, or non-characteristic words etc.</p>
    </div>
    <div class="abs signature" role="img" aria-label="Handwritten signature"></div>
    <div class="abs sign-off">'Lorem<br>ipsum dolor sit amet...'<br>Generate Lorem Ipsum</div>
    <svg class="abs" style="left:0;top:0" width="559" height="790" aria-hidden="true">
      <path d="M474 790 C505 720 500 600 530 540 C540 522 550 512 559 509 L559 790 Z" fill="var(--brand-blue)"/>
    </svg>
    <div class="abs contact web accent">
      <svg class="globe" width="11" height="11" viewBox="0 0 12 12" aria-hidden="true"><g fill="none" stroke="var(--brand-blue)" stroke-width="1"><circle cx="6" cy="6" r="5"/><ellipse cx="6" cy="6" rx="2.2" ry="5"/><line x1="1" y1="6" x2="11" y2="6"/></g></svg>www.glazeworks.ca
    </div>
  </section>

  <!-- Business card front -->
  <section class="sheet card-front">
    <div class="abs wordmark">GLAZEWORKS</div>
  </section>

  <!-- Business card back -->
  <section class="sheet card-back">
    <div class="abs wordmark">GLAZEWORKS</div>
    <div class="abs contact name accent">Reno Vaskelind</div>
    <div class="abs contact details">604-381-4756<br>604-318-5064<br>reno@glazeworks.ca<br><span class="accent">www.glazeworks.ca</span><br>315-27140 62nd Avenue,<br>Langley, BC, V3K 2R8</div>
  </section>
  <div class="abs caption">Business card front &amp; back 2</div>

  <!-- Envelope -->
  <section class="sheet envelope">
    <div class="abs wordmark">GLAZEWORKS</div>
    <div class="abs contact"><span class="accent">p</span> 604-381-4756 <span class="accent">| f</span> 604-318-5064 <span class="accent">| e</span> reno@glazeworks.ca<br><span class="accent">#</span>315-27140 62nd Avenue,Langley, BC, V3K 2R8</div>
  </section>
  <svg class="abs envelope-flap" width="76" height="268" viewBox="0 0 76 268" aria-hidden="true">
    <path d="M0 0 L40 0 Q76 0 76 40 L76 228 Q76 268 40 268 L0 268 Z" fill="var(--brand-blue)"/>
  </svg>
  <div class="abs flap-web">
    <svg class="globe" width="11" height="11" viewBox="0 0 12 12" aria-hidden="true"><g fill="none" stroke="#fff" stroke-width="1"><circle cx="6" cy="6" r="5"/><ellipse cx="6" cy="6" rx="2.2" ry="5"/><line x1="1" y1="6" x2="11" y2="6"/></g></svg>www.glazeworks.ca
  </div>

  <!-- Thank-you card -->
  <section class="sheet thanks-card">
    <svg class="abs" style="left:0;top:0" width="481" height="280" aria-hidden="true">
      <path d="M246 280 C330 250 360 140 420 124 C450 116 470 118 481 120 L481 280 Z" fill="var(--brand-blue)"/>
    </svg>
    <div class="abs thanks-title">Thank You</div>
    <div class="abs wordmark">GLAZEWORKS</div>
    <div class="abs poem">A simple Thanks may not be enough<br>but still we're sending this note to<br>express our heartfelt gratitude<br>Thank you so much for being a part of our big day.<br>We couldn't have made it without you.</div>
    <div class="abs contact signer"><span class="accent">Reno Vaskelind</span> &nbsp;|&nbsp; CEO</div>
    <div class="abs contact web accent">
      <svg class="globe" width="8" height="8" viewBox="0 0 12 12" aria-hidden="true"><g fill="none" stroke="var(--brand-blue)" stroke-width="1.2"><circle cx="6" cy="6" r="5"/><ellipse cx="6" cy="6" rx="2.2" ry="5"/><line x1="1" y1="6" x2="11" y2="6"/></g></svg>www.glazeworks.ca
    </div>
  </section>

</body>
</html>
```